Stonebay Towing Business Card

Towing
Accident towing
Mechanical breakdown
Insurance, salvage and recovery
4wd off road towing
Light & Heavy towing
8347 2516
24 hour business 7 days

Logo can be whole size on front

Industry/Entity Type

Towing/ transport

Contact Information for Business Card

The above

```html
<!DOCTYPE html>
<html lang="en">
<head>
<meta charset="UTF-8">
<title>Stonebay Towing Business Card</title>
<link rel="stylesheet" href="https://fonts.googleapis.com/css2?family=Poppins:wght@500;600;700&display=swap">
<style>
  :root {
    --backdrop: #2e2e2e;
    --card-dark: #151515;
    --card-light: #ffffff;
    --brand-red: #d42027;
    --ink: #111111;
  }
  * { margin: 0; padding: 0; box-sizing: border-box; }
  html, body {
    width: 1200px;
    height: 1000px;
    overflow: hidden;
    background: var(--backdrop);
    font-family: "Poppins", Arial, sans-serif;
  }
  .canvas { position: relative; width: 1200px; height: 1000px; }
  .card {
    position: absolute;
    left: 192px;
    width: 816px;
    height: 466px;
    border-radius: 20px;
    overflow: hidden;
  }
  .card-front {
    top: 24px;
    background: var(--card-dark);
    display: flex;
    align-items: center;
    justify-content: center;
  }
  .brand-name {
    font-weight: 700;
    color: var(--brand-red);
    text-align: center;
    line-height: 1;
    white-space: nowrap;
  }
  .card-front .brand-name { font-size: 72px; }
  .card-back {
    top: 510px;
    background: var(--card-light);
    text-align: center;
  }
  .card-back .brand-name {
    font-size: 46px;
    position: absolute;
    top: 112px;
    left: 0;
    right: 0;
  }
  .hotline {
    position: absolute;
    top: 250px;
    left: 0;
    right: 0;
    display: flex;
    align-items: center;
    justify-content: center;
    gap: 10px;
    color: var(--brand-red);
    font-weight: 600;
    font-size: 24px;
  }
  .hotline svg { width: 34px; height: 34px; }
  .services {
    position: absolute;
    top: 312px;
    left: 0;
    right: 0;
    color: var(--ink);
    font-weight: 500;
    font-size: 22px;
    line-height: 35px;
  }
  .services .divider { color: var(--brand-red); margin: 0 12px; }
  .footer-band {
    position: absolute;
    left: 24px;
    right: 22px;
    bottom: -20px;
    height: 30px;
    background: var(--brand-red);
    border-radius: 14px 14px 0 0;
  }
</style>
</head>
<body>
<main class="canvas">
  <section class="card card-front">
    <div class="brand-name">Stonebay Towing</div>
  </section>

  <section class="card card-back">
    <div class="brand-name">Stonebay Towing</div>

    <div class="hotline">
      <svg viewBox="0 0 34 34" aria-hidden="true">
        <circle cx="17" cy="17" r="17" fill="var(--brand-red)"/>
        <path d="M12.2 9.5c.6-.4 1.4-.3 1.8.3l1.9 2.7c.4.6.3 1.3-.2 1.7l-1.2 1c.8 1.8 2.2 3.3 4 4.2l1-1.2c.4-.5 1.2-.6 1.7-.2l2.7 1.9c.6.4.7 1.2.3 1.8l-1 1.5c-.6.9-1.7 1.3-2.7 1-5-1.4-8.9-5.3-10.3-10.3-.3-1 .1-2.1 1-2.7z" fill="#ffffff"/>
      </svg>
      <span>8347 2516 (24/7 Business)</span>
    </div>

    <div class="services">
      <div>Towing<span class="divider">|</span>Accident Towing<span class="divider">|</span>Mechanical Breakdown</div>
      <div>Insurance, Salvage and Recovery<span class="divider">|</span>4wd Off Road Towing</div>
      <div>Light &amp; Heavy Towing</div>
    </div>

    <div class="footer-band"></div>
  </section>
</main>
</body>
</html>
```